Real State Agency App

We need an app design for a real state agency, we provide mockups for our project that ilustrates very well what we need
our web site is www.brindlevaleestates.com,

Target Market(s)

Tourism

Font styles to use
Other font styles liked:
• attached you will find it

Requirements
Must have
• Colors like the logo

```html
<!DOCTYPE html>
<html lang="en">
<head>
<meta charset="utf-8">
<title>Search – Brindlevale Estates</title>
<link href="https://fonts.googleapis.com/css2?family=Montserrat:wght@400;500;600;700&display=swap" rel="stylesheet">
<style>
  :root{
    --blue:#1d9ed8;
    --blue-dark:#1789bf;
    --divider:#3aa9dc;
    --page:#eef0f2;
    --card:#ffffff;
    --ink:#2f3237;
    --muted:#6a6e74;
    --gold:#e9aa2a;
    --line:#e3e5e8;
    --tab-active:#1d9ed8;
    --tab:#6a6e74;
  }
  *{box-sizing:border-box;margin:0;padding:0}
  html,body{width:675px;height:1200px;overflow:hidden}
  body{font-family:"Montserrat",Arial,sans-serif;background:var(--page);position:relative;color:var(--ink)}
  .topbar{background:var(--blue);color:#fff;height:130px;position:relative}
  .status{height:36px;display:flex;align-items:center;justify-content:space-between;padding:0 14px;font-size:22px;font-weight:500}
  .status .time{position:absolute;left:0;right:0;text-align:center;font-weight:600}
  .status .left,.status .right{display:flex;align-items:center;gap:8px;z-index:1}
  .title{position:absolute;top:58px;left:0;right:0;text-align:center;font-size:27px;font-weight:600}
  .lang{position:absolute;right:22px;top:56px;display:flex;align-items:center;gap:10px;font-size:22px;font-weight:500}
  .filters{display:grid;grid-template-columns:1fr 1fr;background:var(--blue-dark)}
  .filter{height:91px;padding:22px 22px 0;position:relative;color:#fff;border-bottom:2px solid var(--divider)}
  .filter:nth-child(odd){border-right:2px solid var(--divider)}
  .filter:nth-child(n+3){border-bottom:none}
  .filter .label{font-size:16px;font-weight:600;letter-spacing:.5px}
  .filter .value{font-size:25px;font-weight:700;margin-top:4px}
  .filter .key{font-size:25px;font-weight:500;padding-top:8px}
  .filter svg{position:absolute;right:22px;top:34px}
  .card{position:absolute;left:13px;width:649px;background:var(--card);border-radius:6px;overflow:hidden}
  .card.first{top:329px;height:544px}
  .card.second{top:887px;height:260px}
  .photo{height:364px;position:relative;background:linear-gradient(180deg,#8fc0e8 0%,#b7d3b0 35%,#5f8a3e 65%,#4a7a2e 100%)}
  .second .photo{height:260px;background:linear-gradient(180deg,#86b9e6 0%,#e7b6a3 40%,#d9a08d 75%,#b98877 100%)}
  .price{position:absolute;left:0;bottom:0;width:205px;height:68px;background:var(--gold);color:#fff;font-size:24px;font-weight:700;display:flex;align-items:center;padding-left:22px}
  .name{height:85px;display:flex;align-items:center;justify-content:space-between;padding:0 20px 0 22px;border-bottom:2px solid var(--line);font-size:25px;font-weight:600}
  .stats{display:grid;grid-template-columns:repeat(3,1fr);height:95px}
  .stat{display:flex;align-items:center;justify-content:center;gap:12px;font-size:19px;font-weight:500}
  .stat+.stat{border-left:2px solid var(--line)}
  .tabs{position:absolute;left:0;right:0;bottom:0;height:75px;background:#fff;border-top:2px solid var(--line);display:grid;grid-template-columns:repeat(4,1fr)}
  .tab{display:flex;flex-direction:column;align-items:center;justify-content:center;gap:4px;font-size:19px;font-weight:500;color:var(--tab)}
  .tab.active{color:var(--tab-active);font-weight:700}
</style>
</head>
<body>
<header class="topbar">
  <div class="status">
    <div class="left"><span>●●●●●</span><span>Carrier</span>
      <svg width="24" height="18" viewBox="0 0 24 18"><path d="M2 6a14 14 0 0 1 20 0M5 9.5a9 9 0 0 1 14 0M8.5 13a4 4 0 0 1 7 0" stroke="#fff" stroke-width="2.4" fill="none" stroke-linecap="round"/></svg></div>
    <span class="time">9:41 AM</span>
    <div class="right"><span>✱</span><span>100%</span>
      <svg width="44" height="20" viewBox="0 0 44 20"><rect x="1" y="1" width="38" height="18" rx="4" stroke="#fff" stroke-width="2" fill="none"/><rect x="4" y="4" width="32" height="12" rx="2" fill="#fff"/><rect x="40" y="7" width="3" height="6" rx="1" fill="#fff"/></svg></div>
  </div>
  <h1 class="title">Search</h1>
  <div class="lang"><svg width="40" height="26" viewBox="0 0 40 26"><rect width="40" height="26" fill="#2a3f8f"/><path d="M0 0L40 26M40 0L0 26" stroke="#fff" stroke-width="5"/><path d="M0 0L40 26M40 0L0 26" stroke="#c8102e" stroke-width="2"/><path d="M20 0V26M0 13H40" stroke="#fff" stroke-width="8"/><path d="M20 0V26M0 13H40" stroke="#c8102e" stroke-width="4.5"/></svg>English</div>
</header>

<section class="filters">
  <div class="filter"><div class="label">LOOKING FOR</div><div class="value">To Buy</div>
    <svg width="22" height="14" viewBox="0 0 22 14"><path d="M2 2l9 9 9-9" stroke="#fff" stroke-width="2.6" fill="none"/></svg></div>
  <div class="filter"><div class="key">Key</div>
    <svg width="26" height="26" viewBox="0 0 26 26"><circle cx="13" cy="13" r="12" fill="#fff"/><path d="M7 13h11M13 8l5 5-5 5" stroke="var(--blue-dark)" stroke-width="2.6" fill="none"/></svg></div>
  <div class="filter"><div class="label">TYPE</div><div class="value">House</div>
    <svg width="22" height="14" viewBox="0 0 22 14"><path d="M2 2l9 9 9-9" stroke="#fff" stroke-width="2.6" fill="none"/></svg></div>
  <div class="filter"><div class="label">AREA</div><div class="value">Palma</div>
    <svg width="22" height="14" viewBox="0 0 22 14"><path d="M2 2l9 9 9-9" stroke="#fff" stroke-width="2.6" fill="none"/></svg></div>
</section>

<article class="card first">
  <div class="photo" role="img" aria-label="Single-storey white villa on a green lawn among pine trees">
    <div class="price">1,000,000 €</div>
  </div>
  <div class="name"><span>Villa Son Servera, Mallorca, Baleares</span>
    <svg width="14" height="24" viewBox="0 0 14 24"><path d="M2 2l10 10-10 10" stroke="#777" stroke-width="2.4" fill="none"/></svg></div>
  <div class="stats">
    <div class="stat"><svg width="32" height="22" viewBox="0 0 32 22"><path d="M2 20V4M2 14h28v6M30 14v-3a3 3 0 0 0-3-3H13v6M6 11a2.5 2.5 0 1 0 0-.1" stroke="var(--gold)" stroke-width="2.2" fill="none"/></svg>4 Bedrooms</div>
    <div class="stat"><svg width="34" height="22" viewBox="0 0 34 22"><path d="M2 4h30M5 4v8a7 7 0 0 0 7 7h10a7 7 0 0 0 7-7V4M9 19l-2 3M25 19l2 3" stroke="var(--gold)" stroke-width="2.2" fill="none"/></svg>3 Bathrooms</div>
    <div class="stat"><svg width="26" height="26" viewBox="0 0 26 26"><path d="M3 23L23 3M13 3h10v10M3 13v10h10" stroke="var(--gold)" stroke-width="2.4" fill="none"/></svg>206 (m²)</div>
  </div>
</article>

<article class="card second">
  <div class="photo" role="img" aria-label="Two-storey pink house with white balcony under a blue sky"></div>
</article>

<nav class="tabs">
  <div class="tab active"><svg width="30" height="30" viewBox="0 0 30 30"><circle cx="17" cy="12" r="9" stroke="currentColor" stroke-width="2.4" fill="none"/><path d="M10 19l-7 8" stroke="currentColor" stroke-width="2.6"/></svg>Search</div>
  <div class="tab"><svg width="30" height="30" viewBox="0 0 30 30"><path d="M16 2h11v11L14 27 2 15z" stroke="currentColor" stroke-width="2.2" fill="none"/><circle cx="21" cy="8" r="2" fill="currentColor"/></svg>Sell</div>
  <div class="tab"><svg width="30" height="30" viewBox="0 0 30 30"><circle cx="15" cy="15" r="4.5" stroke="currentColor" stroke-width="2.2" fill="none"/><path d="M15 3v4M15 23v4M3 15h4M23 15h4M6.5 6.5l3 3M20.5 20.5l3 3M6.5 23.5l3-3M20.5 9.5l3-3" stroke="currentColor" stroke-width="2.6"/><circle cx="15" cy="15" r="8.5" stroke="currentColor" stroke-width="2.2" fill="none"/></svg>Our Services</div>
  <div class="tab"><svg width="30" height="30" viewBox="0 0 30 30"><path d="M3 3h24v18H12l-6 6v-6H3z" stroke="currentColor" stroke-width="2.2" fill="none"/><circle cx="10" cy="12" r="1.6" fill="currentColor"/><circle cx="15" cy="12" r="1.6" fill="currentColor"/><circle cx="20" cy="12" r="1.6" fill="currentColor"/></svg>Contact</div>
</nav>
</body>
</html>
```